New Bicycle shop business card

Hi!
I'm looking for a business card for my new proffesional bike mechanics shop. This shop is only for fixing broken bikes and not selling bikes.
Peferbly a modern and sleek and modern design.
Colors: black, grey, red, white
Information:
Name: Rijwielwerkplaats Vanhoutem
Shop owner: Bart Vanhoutem & Sanne Maertens
Website: www.rijwielwerkplaats-vanhoutem.be
Email: info@rijwielwerkplaats-vanhoutem.be
Phone number: +32471902386
Street adres: Kerkweg 64
9970 Oostmoere
Slogan/shop information: Herstellingen van alle merken.
Logo: see files.
Target Market(s)
People who seek a mechanic to fix or upgrade their bikes.
Contact Information for Business Card
Information:
Website: info@rijwielwerkplaats-vanhoutem.be
9970 Oostmoere
Logo: see files.

```html
<!DOCTYPE html>
<html lang="nl">
<head>
<meta charset="utf-8">
<title>Rijwielwerkplaats Vanhoutem – visitekaartje</title>
<link rel="stylesheet" href="https://fonts.googleapis.com/css2?family=Montserrat:wght@400;700;800&family=Open+Sans:wght@400;600&display=swap">
<style>
  :root {
    --ink: #0c0c0d;
    --red: #e8294a;
    --grey: #a7a9ab;
    --white: #ffffff;
    --text: #2b2b2b;
    --backdrop: #2a2c30;
  }
  * { box-sizing: border-box; margin: 0; padding: 0; }
  html, body { width: 1200px; height: 900px; overflow: hidden; }
  body {
    background: var(--backdrop);
    display: flex;
    align-items: center;
    justify-content: center;
    gap: 40px;
    font-family: "Open Sans", sans-serif;
  }
  .card {
    position: relative;
    width: 540px;
    height: 348px;
    overflow: hidden;
    box-shadow: 0 14px 34px rgba(0,0,0,.45);
  }

  /* Front */
  .card-front {
    background: var(--ink);
    display: flex;
    align-items: center;
    justify-content: center;
    gap: 22px;
  }
  .brand-mark {
    width: 54px; height: 54px;
    background: var(--red);
    flex: none;
  }
  .brand-name {
    font-family: "Montserrat", sans-serif;
    font-weight: 800;
    color: var(--white);
    font-size: 27px;
    line-height: 1.25;
    letter-spacing: 2px;
    text-transform: uppercase;
  }

  /* Back */
  .card-back { background: var(--white); }
  .accent-strip {
    position: absolute; left: 0; top: 0;
    width: 9px; height: 196px;
    background: var(--red);
  }
  .owner {
    position: absolute; left: 9px;
    padding: 0 20px;
    display: flex; flex-direction: column; justify-content: center;
  }
  .owner-primary { top: 0; width: 300px; height: 110px; background: var(--grey); }
  .owner-secondary { top: 118px; width: 236px; height: 78px; background: var(--ink); }
  .owner-name {
    font-family: "Montserrat", sans-serif;
    font-weight: 800;
    font-size: 17px;
    letter-spacing: .5px;
    text-transform: uppercase;
  }
  .owner-role {
    font-family: "Montserrat", sans-serif;
    font-size: 10px;
    text-transform: uppercase;
    margin-top: 2px;
  }
  .owner-primary .owner-name { color: var(--ink); }
  .owner-primary .owner-role { color: #3a3a3a; }
  .owner-secondary .owner-name, .owner-secondary .owner-role { color: var(--white); }

  .slogan {
    position: absolute; left: 318px; top: 44px; width: 210px;
    font-family: "Montserrat", sans-serif;
    font-weight: 700;
    font-size: 15px;
    line-height: 1.35;
    color: var(--red);
  }
  .contact-list {
    position: absolute; left: 262px; top: 128px;
    list-style: none;
  }
  .contact-item {
    display: flex; align-items: flex-start; gap: 12px;
    font-size: 13px; color: var(--text);
    margin-bottom: 12px; line-height: 1.3;
  }
  .contact-icon {
    width: 24px; height: 24px; flex: none;
    border-radius: 50%;
    background: var(--red);
    display: flex; align-items: center; justify-content: center;
  }
  .contact-icon svg { width: 13px; height: 13px; }
  .contact-text { padding-top: 3px; }
</style>
</head>
<body>

  <section class="card card-front" aria-label="Voorkant visitekaartje">
    <div class="brand-mark"></div>
    <h1 class="brand-name">Rijwielwerkplaats<br>Vanhoutem</h1>
  </section>

  <section class="card card-back" aria-label="Achterkant visitekaartje">
    <div class="accent-strip"></div>
    <div class="owner owner-primary">
      <p class="owner-name">Bart Vanhoutem</p>
      <p class="owner-role">Owner</p>
    </div>
    <div class="owner owner-secondary">
      <p class="owner-name">Sanne Maertens</p>
      <p class="owner-role">Owner</p>
    </div>

    <p class="slogan">Herstellingen van alle merken</p>

    <ul class="contact-list">
      <li class="contact-item">
        <span class="contact-icon"><svg viewBox="0 0 24 24" fill="#fff"><path d="M6.6 10.8a15.1 15.1 0 0 0 6.6 6.6l2.2-2.2c.3-.3.7-.4 1-.2 1.1.4 2.3.6 3.6.6.6 0 1 .4 1 1V20c0 .6-.4 1-1 1A17 17 0 0 1 3 4c0-.6.4-1 1-1h3.5c.6 0 1 .4 1 1 0 1.3.2 2.5.6 3.6.1.3 0 .7-.2 1z"/></svg></span>
        <span class="contact-text">+32 471 90 23 86</span>
      </li>
      <li class="contact-item">
        <span class="contact-icon"><svg viewBox="0 0 24 24" fill="#fff"><path d="M3 5h18v14H3z" /><path d="M3 5l9 7 9-7" fill="none" stroke="#e8294a" stroke-width="1.8"/></svg></span>
        <span class="contact-text">info@rijwielwerkplaats-vanhoutem.be</span>
      </li>
      <li class="contact-item">
        <span class="contact-icon"><svg viewBox="0 0 24 24" fill="none" stroke="#fff" stroke-width="2"><circle cx="12" cy="12" r="9"/><path d="M3 12h18M12 3c3 3.3 3 14.7 0 18M12 3c-3 3.3-3 14.7 0 18"/></svg></span>
        <span class="contact-text">www.rijwielwerkplaats-vanhoutem.be</span>
      </li>
      <li class="contact-item">
        <span class="contact-icon"><svg viewBox="0 0 24 24" fill="#fff"><path d="M12 2a7 7 0 0 0-7 7c0 5.2 7 13 7 13s7-7.8 7-13a7 7 0 0 0-7-7zm0 9.5A2.5 2.5 0 1 1 12 6.5a2.5 2.5 0 0 1 0 5z"/></svg></span>
        <span class="contact-text">Kerkweg 64<br>9970 Oostmoere</span>
      </li>
    </ul>
  </section>

</body>
</html>
```